Flyer / Mailer for Business Debt Relief Business - Harborline Relief 6" x 11"

We need a 6" x 11" double sided flyer. This will be sent out to potential customers with high interest business loans. We would like the design to coordinate with the colors of our logo. I have included a mock up that we sketched out. I have also included a file of a mailer we received that we would like to use as a template (not colors or fonts, just set up). I have also included an .ai file of our logo.

```html
<!DOCTYPE html>
<html lang="en">
<head>
<meta charset="utf-8">
<title>Harborline Relief – Business Debt Relief Mailer</title>
<link href="https://fonts.googleapis.com/css2?family=Montserrat:wght@400;500;600&display=swap" rel="stylesheet">
<style>
  :root {
    --page: #f4f4f4;
    --paper: #ffffff;
    --green: #7cc04a;
    --green-deep: #6aae3b;
    --blue: #1b87c9;
    --blue-deep: #1566a6;
    --ink: #2f2f2f;
    --ink-soft: #4a4a4a;
    --rule: #8a8a8a;
  }
  * { box-sizing: border-box; margin: 0; padding: 0; }
  html, body { width: 1200px; height: 900px; overflow: hidden; }
  body {
    background: var(--page);
    font-family: "Montserrat", Arial, sans-serif;
    color: var(--ink);
    position: relative;
  }
  .mailer-side {
    position: absolute;
    left: 230px;
    width: 740px;
    height: 404px;
    background: var(--paper);
    overflow: hidden;
    box-shadow: 0 2px 10px rgba(0,0,0,.08);
  }
  .side-front { top: 32px; }
  .side-back { top: 464px; }

  /* Front side */
  .photo-column { position: absolute; left: 0; top: 0; width: 160px; height: 404px; }
  .photo-tile { width: 160px; height: 101px; }
  .photo-tile + .photo-tile { border-top: 2px solid var(--paper); }
  .tile-savings { background: linear-gradient(160deg, #b9c4cc, #8e9ea8); }
  .tile-handshake { background: linear-gradient(160deg, #d9d2c8, #a99c8c); }
  .tile-meeting { background: linear-gradient(160deg, #eef0f3, #c9d3de); }
  .tile-coins { background: linear-gradient(160deg, #4f6f8c, #223a52); }

  .front-header { position: absolute; left: 160px; top: 0; right: 0; height: 61px; }
  .tagline {
    position: absolute; left: 45px; top: 24px;
    font-size: 12.5px; font-weight: 500; letter-spacing: .2px; color: var(--ink);
  }
  .tagline .accent { color: var(--green); }
  .brand-mark {
    position: absolute; display: flex; align-items: center; gap: 7px;
    font-weight: 500; color: var(--ink-soft); letter-spacing: 1px; text-transform: uppercase;
  }
  .front-header .brand-mark { right: 40px; top: 20px; font-size: 10.5px; }
  .brand-square { width: 18px; height: 18px; background: var(--green); flex: none; }

  .front-body {
    position: absolute; left: 160px; top: 61px; right: 0; height: 240px;
    background: linear-gradient(90deg, #ffffff 0%, #f4f7fa 45%, #dfe8f0 100%);
  }
  .advisor-photo {
    position: absolute; right: 0; top: 0; width: 250px; height: 240px;
    background: linear-gradient(100deg, rgba(223,232,240,0) 0%, #c9d7e3 35%, #8aa4bc 70%, #2d3f5c 100%);
  }
  .green-band {
    position: absolute; left: 160px; top: 61px; right: 0; height: 54px;
    background: linear-gradient(90deg, var(--green) 70%, var(--green-deep) 100%);
    clip-path: polygon(0 0, 100% 0, 100% 55%, 78% 100%, 0 100%);
  }
  .band-copy {
    position: absolute; left: 45px; top: 10px;
    font-size: 15.5px; line-height: 17.5px; color: #fff; letter-spacing: .3px;
  }
  .band-copy strong { font-weight: 600; }

  .help-block { position: absolute; left: 205px; top: 133px; width: 330px; }
  .help-question { font-size: 12px; font-weight: 500; color: var(--ink); }
  .help-answer { font-size: 12.5px; font-weight: 600; color: var(--blue); margin-top: 2px; }
  .benefit-list { list-style: none; margin-top: 10px; }
  .benefit-list li {
    position: relative; padding-left: 17px;
    font-size: 9.8px; line-height: 12.7px; color: var(--ink);
  }
  .benefit-list li::before {
    content: ""; position: absolute; left: 2px; top: 5px;
    width: 3px; height: 3px; border-radius: 50%; background: var(--ink);
  }

  .contact-band {
    position: absolute; left: 160px; top: 301px; right: 0; bottom: 0;
    background: var(--blue);
  }
  .contact-band svg { position: absolute; right: 0; top: 0; }
  .contact-web { position: absolute; left: 45px; top: 27px; color: #fff; }
  .contact-label { font-size: 11px; }
  .contact-url { font-size: 15.5px; margin-top: 3px; }
  .contact-email { font-size: 10.5px; margin-top: 3px; }
  .contact-call { position: absolute; left: 287px; top: 27px; color: #fff; }
  .contact-call .contact-label { line-height: 13px; }
  .contact-call strong { font-weight: 600; }
  .contact-phone { font-size: 18px; letter-spacing: .6px; margin-top: 4px; }

  /* Back side */
  .return-block { position: absolute; left: 56px; top: 62px; width: 148px; text-align: center; }
  .side-back .brand-mark { position: static; justify-content: center; font-size: 11.5px; flex-direction: column; gap: 8px; }
  .side-back .brand-square { width: 32px; height: 32px; }
  .return-rule { height: 1px; background: var(--rule); margin: 14px 0 11px; }
  .return-address { font-size: 11px; line-height: 14px; color: var(--ink); }
  .back-headline {
    position: absolute; left: 33px; top: 240px;
    font-size: 17.5px; line-height: 22px; font-weight: 400; color: var(--blue);
  }
  .back-copy {
    position: absolute; left: 33px; top: 300px; width: 260px;
    font-size: 10.8px; line-height: 15px; color: var(--ink);
  }
</style>
</head>
<body>

<section class="mailer-side side-front" aria-label="Mailer front">
  <div class="photo-column">
    <div class="photo-tile tile-savings" role="img" aria-label="Photo of hands sheltering a jar of cash savings"></div>
    <div class="photo-tile tile-handshake" role="img" aria-label="Photo of a smiling business owner handing cash across a counter"></div>
    <div class="photo-tile tile-meeting" role="img" aria-label="Photo of a financial meeting with tablet and charts"></div>
    <div class="photo-tile tile-coins" role="img" aria-label="Photo of stacked coins with a rising financial graph"></div>
  </div>

  <div class="front-body">
    <div class="advisor-photo" role="img" aria-label="Photo of a smiling consultant in a suit holding a phone by an office window"></div>
  </div>

  <header class="front-header">
    <p class="tagline">Helping Business <span class="accent">Focus</span> On What Matters!</p>
    <div class="brand-mark"><span class="brand-square"></span>Harborline Relief</div>
  </header>

  <div class="green-band">
    <p class="band-copy">We understand that merchant cash advance<br>loads can be a <strong>burden on your business</strong></p>
  </div>

  <div class="help-block">
    <p class="help-question">Overwhelmed by daily/weekly payments?</p>
    <p class="help-answer">WE CAN HELP!</p>
    <ul class="benefit-list">
      <li>This is not a load, WE ARE NOT LENDERS</li>
      <li>Improve your business cash flow immediately</li>
      <li>Move payments to one monthly amount</li>
      <li>Reduce the amount you are paying out monthly</li>
      <li>Strategic alternatives to high interest loads</li>
      <li>Fast,confidential business debt relief</li>
      <li>No-obligation consultation</li>
      <li>Absolutely no credit pulls</li>
      <li>No collateral, no financials</li>
    </ul>
  </div>

  <footer class="contact-band">
    <svg width="250" height="40" viewBox="0 0 250 40" aria-hidden="true">
      <polygon points="0,0 250,0 250,38" fill="#1566a6"/>
    </svg>
    <div class="contact-web">
      <p class="contact-label">Visit our website:</p>
      <p class="contact-url">www.harborlinetoday.com</p>
      <p class="contact-email">Email: info@harborlinetoday.com</p>
    </div>
    <div class="contact-call">
      <p class="contact-label">Call now for <strong>free</strong><br>consulation with our experts</p>
      <p class="contact-phone">800-555-0142</p>
    </div>
  </footer>
</section>

<section class="mailer-side side-back" aria-label="Mailer back">
  <div class="return-block">
    <div class="brand-mark"><span class="brand-square"></span>Harborline Relief</div>
    <div class="return-rule"></div>
    <p class="return-address">1450 W Marina Dr<br>Harbor City, TX 76100</p>
  </div>
  <h1 class="back-headline">Strategic Debt Relief For<br>Business Of All Sizes</h1>
  <p class="back-copy">Stop taking loads to pay off other loans. Take back your business cash flow, and focus on what matters.</p>
</section>

</body>
</html>
```